New homepage design www.quillharbor.nl

We need a new website design to go with our new designed logo.
We are a relativly small basketballclub that would like a shiny new webdesign for our homepage. We want te be able to create a real homepage/base for our clubmembers, where they can find news, upcoming events (agenda/calendar) and the related info on playing basketball at our club (games/tasks/teams and all).

The current website is located at: www.quillharbor.nl but is an outdated and not so appealing design.
There are no real designfeatures of the current site that have to be transferred to the new site.
Coding in HTML/CSS/JS/JPEG/PNG is enough, making a dynamic website will be my task. I just need the design in HTML (preferrably HTML 5)

There is not a huge budget, we are a club without a main sponsor.

Feel free to be creative and amaze us!

Text for the page in the new design will be created by us, you may use some sample text for filling.

Currently used pictures in the site don't have to be transferred to the new page (preferrably not!)
Updates

Tomorrow we will pick a design.

Industry/Entity Type

Events

Requirements
Must have
• The new logo as uploaded and attached.
News page.
Agenda page
HTML compatible same look and feel in all modern browsers (IE, FireFox, Chrome, Safari)
Nice to have
• HTML 5 validated and approved

```html
<!DOCTYPE html>
<html lang="en">
<head>
<meta charset="utf-8">
<title>Quillharbor Basketball – Home</title>
<link rel="stylesheet" href="https://fonts.googleapis.com/css2?family=Oswald:wght@400;500;700&family=Open+Sans:wght@400;700&display=swap">
<style>
  :root {
    --navy: #1f3a54;
    --orange: #f28c2a;
    --grey-dark: #6d6e70;
    --grey-panel: #737476;
    --grey-nav: #7a7b7d;
    --hero-top: #f1f1f1;
    --hero-bottom: #c8c8c8;
    --white: #ffffff;
    --rule: #d6d6d6;
    --footer-text: #555555;
    --footer-muted: #9a9a9a;
    --icon: #a9a9a9;
    --frame: #c9c9c9;
  }
  * { box-sizing: border-box; margin: 0; padding: 0; }
  html, body { width: 1049px; height: 1200px; overflow: hidden; background: var(--white); }
  body { position: relative; font-family: "Open Sans", Arial, sans-serif; }

  .hero {
    position: absolute; left: 0; top: 0; width: 1049px; height: 576px;
    background: linear-gradient(180deg, var(--hero-top) 0%, var(--hero-bottom) 100%);
    overflow: hidden;
  }
  .hero-art {
    position: absolute; left: 372px; top: 0; width: 677px; height: 576px;
    background: linear-gradient(160deg, rgba(31,58,84,0.18) 0%, rgba(242,140,42,0.22) 55%, rgba(200,200,200,0) 100%);
  }
  .brand {
    position: absolute; left: 42px; top: 72px; display: flex; align-items: center; gap: 8px;
  }
  .brand-dot { width: 34px; height: 34px; border-radius: 50%; background: var(--orange); }
  .brand-name {
    font-family: "Oswald", sans-serif; font-weight: 700; font-size: 27px; color: var(--navy); letter-spacing: 0.5px;
  }

  .main-nav {
    position: absolute; left: 229px; top: 27px; width: 799px; height: 48px;
    background: var(--navy); box-shadow: 4px 4px 0 var(--grey-nav);
    display: flex; align-items: stretch;
  }
  .main-nav a {
    display: flex; align-items: center; padding: 0 15.5px;
    font-family: "Oswald", sans-serif; font-weight: 500; font-size: 21px; color: var(--white);
    text-decoration: none; text-transform: uppercase;
  }
  .main-nav a.is-active { background: var(--grey-nav); }

  .welcome-title {
    position: absolute; left: 47px; top: 222px;
    font-family: "Oswald", sans-serif; font-weight: 700; font-size: 72px; line-height: 1; color: var(--navy);
    letter-spacing: 0.5px;
  }
  .welcome-text {
    position: absolute; left: 50px; top: 310px; width: 330px;
    font-family: "Oswald", sans-serif; font-weight: 700; font-size: 39px; line-height: 48px; color: var(--grey-dark);
  }
  .welcome-text .accent { color: var(--orange); }

  .notice-band {
    position: absolute; left: 0; top: 576px; width: 1049px; height: 144px;
    background: var(--navy); color: var(--white);
    padding: 22px 34px 0 29px; font-size: 14.2px; line-height: 17.5px;
  }

  .announcements {
    position: absolute; left: 9px; top: 743px; width: 483px; height: 341px;
    background: var(--orange); color: var(--white); padding: 16px 14px 0 14px;
  }
  .panel-title {
    font-family: "Oswald", sans-serif; font-weight: 500; font-size: 29px; line-height: 1; text-transform: uppercase;
  }
  .announcements p { margin-top: 12px; font-size: 12.2px; line-height: 15.5px; padding-right: 20px; }
  .dates { list-style: none; margin-top: 10px; font-size: 12.2px; line-height: 15.4px; }
  .dates li { position: relative; padding-left: 16px; }
  .dates li::before {
    content: ""; position: absolute; left: 1px; top: 5px; width: 6px; height: 6px; border-radius: 50%; background: var(--white);
  }
  .read-more {
    position: absolute; left: 14px; bottom: 20px;
    font-family: "Oswald", sans-serif; font-weight: 500; font-size: 21px; color: var(--white); text-decoration: none;
  }
  .read-more span { font-size: 14px; }

  .teams {
    position: absolute; left: 503px; top: 743px; width: 535px; height: 185px;
    background: var(--grey-panel); color: var(--white); padding: 12px 18px 0 19px;
  }
  .teams .panel-title { font-size: 28px; }
  .team-columns { display: flex; gap: 45px; margin-top: 8px; }
  .team-list { list-style: none; width: 223px; }
  .team-list li {
    font-size: 12.5px; line-height: 23px; height: 25px; border-bottom: 1px solid var(--white);
  }

  .gallery { position: absolute; left: 503px; top: 935px; width: 535px; }
  .gallery-head { display: flex; justify-content: space-between; align-items: baseline; padding: 0 3px 0 4px; }
  .gallery-title {
    font-family: "Oswald", sans-serif; font-weight: 500; font-size: 33px; line-height: 1; color: var(--grey-dark);
  }
  .gallery-more {
    font-family: "Oswald", sans-serif; font-weight: 400; font-size: 20px; color: var(--grey-dark); text-decoration: none;
  }
  .photo {
    position: absolute; top: 47px; height: 99px; border: 4px solid var(--frame);
    background: linear-gradient(180deg, #9aa3b4 0%, #4f6fae 50%, #b59a78 100%);
  }
  .photo.p1 { left: 5px; width: 151px; }
  .photo.p2 { left: 169px; width: 134px; background: linear-gradient(180deg, #a8a6a0 0%, #8d8a84 50%, #b89a76 100%); }
  .photo.p3 { left: 317px; width: 99px; }
  .photo.p4 { left: 431px; width: 104px; background: linear-gradient(180deg, #a8a6a0 0%, #8d8a84 50%, #b89a76 100%); }

  .site-footer {
    position: absolute; left: 0; top: 1111px; width: 1049px; height: 89px; border-top: 2px solid var(--rule);
  }
  .footer-nav { position: absolute; left: 14px; top: 18px; display: flex; gap: 18px; }
  .footer-nav a {
    font-family: Arial, Helvetica, sans-serif; font-size: 13.5px; color: var(--footer-text); text-decoration: none; text-transform: uppercase;
  }
  .copyright {
    position: absolute; left: 14px; top: 40px;
    font-family: Arial, Helvetica, sans-serif; font-size: 11px; color: var(--footer-muted);
  }
  .social { position: absolute; left: 746px; top: 22px; display: flex; gap: 9px; }
  .social span { width: 30px; height: 30px; border-radius: 50%; background: var(--icon); display: block; }
  .footer-brand {
    position: absolute; left: 950px; top: 26px;
    font-family: "Oswald", sans-serif; font-weight: 700; font-size: 14px; color: var(--footer-muted);
  }
</style>
</head>
<body>

<header class="hero">
  <div class="hero-art" role="img" aria-label="Illustration of a basketball player leaping toward a hoop with ball in hand"></div>

  <div class="brand">
    <span class="brand-dot"></span>
    <span class="brand-name">QUILLHARBOR</span>
  </div>

  <nav class="main-nav">
    <a href="#" class="is-active">Home</a>
    <a href="#">Teams</a>
    <a href="#">Information</a>
    <a href="#">Gallery</a>
    <a href="#">Contact</a>
    <a href="#">Links</a>
    <a href="#">Guestbook</a>
    <a href="#">Login</a>
  </nav>

  <h1 class="welcome-title">WELKOM</h1>
  <p class="welcome-text">Het bestuur van BC <span class="accent">Quillharbor</span> heet je welkom op onze site.</p>
</header>

<section class="notice-band">
  <p><strong>CLOTHING:</strong> If you do not yet have complete basketball clothes, think of Kestrel Hoops. Quill Harbor is going to work. These sports in Dunvale together This sporting goods store has all the necessary stuff for basketball. Think of shoes, a dress or suits. The choice is well represented, and there is also a nice discount on! So if you need new stuff, then just walk in Kestrel Hoops in Dunvale inside. Indicate that you are a member of Quill Harbor and the discount will be deducted. Of all purchases from members of Quill Harbor association gets as a small amount. This will be invested in new materials. Thus, our association members both helped!</p>
</section>

<section class="announcements">
  <h2 class="panel-title">Important Announcements:</h2>
  <p>IMPORTANT DATES: throughout the season, there are a few dates that we are unfortunately not able to make use of the sports hall or gymnasium Ashmoor Hall use. Ther are also a number of important other data. Consider the transition from the Tuesday of the sports hall to hall Ashmoor Hall (and back again). Below is a summary of these important dates:</p>
  <ul class="dates">
    <li>31-12-2013 No training related New Year's Eve</li>
    <li>20-02-2014 No training related carnival</li>
    <li>24-02-2014 No training related carnival</li>
    <li>25-02-2014 No training related carnival</li>
    <li>27-02-2014 No training related carnival</li>
    <li>03-03-2014 No training related carnival</li>
    <li>04-03-2014 No training related carnival</li>
  </ul>
  <a href="#" class="read-more">READ MORE <span>+</span></a>
</section>

<section class="teams">
  <h2 class="panel-title">Teams</h2>
  <div class="team-columns">
    <ul class="team-list">
      <li>01. Ladies Recreaten 1</li>
      <li>02. Seneor Women 1</li>
      <li>03. Externals</li>
      <li>04. Recereaten Men</li>
      <li>05. Seneor Men 1</li>
    </ul>
    <ul class="team-list">
      <li>Ladies Recreaten 1</li>
      <li>Seneor Women 1</li>
      <li>Externals</li>
      <li>Recereaten Men</li>
      <li>Seneor Men 1</li>
    </ul>
  </div>
</section>

<section class="gallery">
  <div class="gallery-head">
    <h2 class="gallery-title">GALLERY</h2>
    <a href="#" class="gallery-more">MORE</a>
  </div>
  <div class="photo p1" role="img" aria-label="Team photo of players in blue kit in a sports hall"></div>
  <div class="photo p2" role="img" aria-label="Players sitting on a sports hall floor"></div>
  <div class="photo p3" role="img" aria-label="Team photo of players in blue kit in a sports hall"></div>
  <div class="photo p4" role="img" aria-label="Players sitting on a sports hall floor"></div>
</section>

<footer class="site-footer">
  <nav class="footer-nav">
    <a href="#">Home</a>
    <a href="#">Teams</a>
    <a href="#">Information</a>
    <a href="#">Gallery</a>
    <a href="#">Contact</a>
    <a href="#">Links</a>
    <a href="#">Guestbook</a>
    <a href="#">Login</a>
  </nav>
  <p class="copyright">© Copyright 2002 - 2013 Company Name. All Rights Reserved</p>
  <div class="social" aria-label="Social networks">
    <span></span><span></span><span></span>
  </div>
  <span class="footer-brand">QUILLHARBOR</span>
</footer>

</body>
</html>
```